Design a Website User Interface for QRcode generation company

We’re new and innovative company to allow visitors to create QRcodes directly from our website. Our url is: plimvota(dot)net
We’re looking for a design of our home page user interface. Just like many companies these days have the home page as a functional landing page instead of welcome text (hueblend(dot)com, tabmark(dot)cc, etc), we too are looking to have a page where the user can go, and right from the home page can start creating a product.
The functionality will be similar to codevault(dot)com, but we will allow the visitor to upload their images. Then the user will be able to draw a square on that picture and the QRcode will be placed inside that square.
In short, the user will have to perform 5 steps:
1 select what kind of QRcode to create (url, sms, address, contact info, etc)
2 fill-in the information required for that type of QRcode
3 upload the image (including button to upload, drag-images-here, etc, image preview area after uploaded, etc)
4 draw a square on top of the uploaded image
5 verify and download the produced output image
The idea is similar to what can be seen on telvoris(dot)com/qrcode/ site, but needs to be much simpler to navigate.

We like modern clear style for our website, but we would also like to see colors, however the main background should stay relatively clear.

Good luck to you all,

```html
<!DOCTYPE html>
<html lang="en">
<head>
<meta charset="utf-8">
<title>Plimvota – Generate your own QR Code</title>
<link href="https://fonts.googleapis.com/css2?family=Lato:wght@400;700;900&family=Gochi+Hand&display=swap" rel="stylesheet">
<style>
:root{
  --yellow:#f4c20d;
  --ink:#3d4347;
  --text:#6d757a;
  --muted:#9aa2a7;
  --line:#dde2e5;
  --band:#eceff1;
  --stage:#e6eaec;
  --tab:#e1e6e9;
  --white:#ffffff;
}
*{box-sizing:border-box;margin:0;padding:0}
html,body{width:1200px;height:808px;overflow:hidden}
body{font-family:'Lato',sans-serif;color:var(--text);background:var(--white);position:relative}
.abs{position:absolute}

.top-rule{left:0;top:0;width:1200px;height:4px;background:var(--yellow)}
.header{left:0;top:4px;width:1200px;height:161px;background:var(--white)}
.brand{left:111px;top:46px;width:100px;font:900 30px/30px 'Lato',sans-serif;color:var(--yellow);letter-spacing:-0.3px}
.tagline{left:227px;top:48px;font:28px/30px 'Gochi Hand',cursive;color:var(--ink);letter-spacing:1px}

.field{height:33px;border:1px solid var(--line);background:var(--white);font-size:12px;color:var(--muted);display:flex;align-items:center;padding-left:10px;gap:8px}
.field svg{flex:none}
.field.user{left:688px;top:55px;width:132px}
.field.pass{left:829px;top:55px;width:131px}
.btn{background:var(--yellow);display:flex;align-items:center;justify-content:center}
.btn.login{left:969px;top:55px;width:33px;height:33px}
.account-links{left:780px;top:96px;width:226px;text-align:right;font-size:11.5px;color:var(--text)}
.account-links span{margin-left:10px;color:var(--ink)}

.nav-band{left:0;top:165px;width:1200px;height:72px;background:var(--band);border-top:1px solid var(--line);border-bottom:1px solid var(--line)}
.nav{left:112px;top:165px;height:72px;display:flex;border-left:1px solid var(--line)}
.nav-item{height:72px;display:flex;align-items:center;justify-content:center;font:700 14px 'Lato',sans-serif;color:var(--ink);border-right:1px solid var(--line);gap:10px}
.nav-item.active{background:var(--white);border-top:3px solid var(--yellow)}

.stage{left:0;top:237px;width:1200px;height:376px;background:var(--stage)}
.section-title{left:112px;top:252px;width:271px;height:41px;background:var(--yellow);color:var(--white);font:400 18px/41px 'Lato',sans-serif;text-align:center}
.section-title b{font-weight:900}
.title-pointer{left:236px;top:292px}
.section-rule{left:383px;top:292px;width:704px;height:1px;background:#d3d9dc}

.steps{left:112px;top:321px;width:975px;height:63px;display:flex}
.step{width:195px;height:63px;background:var(--tab);border:1px solid #d5dbde;border-left:none;display:flex;align-items:center;padding-left:18px;gap:12px;font:700 15px 'Lato',sans-serif;color:#5b6267}
.step:first-child{border-left:1px solid #d5dbde}
.step.active{background:var(--white);border-bottom-color:var(--white);color:var(--yellow)}
.step-num{width:30px;height:30px;border-radius:50%;background:#a3abb0;color:var(--white);font-size:14px;display:flex;align-items:center;justify-content:center}
.step.active .step-num{background:var(--yellow)}

.panel{left:112px;top:383px;width:975px;height:181px;background:var(--white);border:1px solid #d5dbde;border-top:none}
.type-list{list-style:none;top:402px;font-size:14.5px;color:var(--muted)}
.type-list li{height:30px;display:flex;align-items:center;gap:14px}
.type-list li::before{content:"";width:9px;height:9px;border-radius:50%;border:2px solid #a3abb0}
.type-list li.selected{color:var(--ink)}
.type-list li.selected::before{background:var(--yellow);border-color:var(--yellow)}
.col-a{left:137px}.col-b{left:353px}.col-c{left:571px}

.footer-rule{left:0;top:613px;width:1200px;height:3px;background:var(--yellow)}
.footer-heading{top:636px;font:900 13px 'Lato',sans-serif;color:var(--ink)}
.footer-text{font-size:11px;line-height:19px;color:var(--text)}
.footer-text b{color:var(--ink)}
.about{left:112px;top:669px;width:225px}
.news-note{left:361px;top:669px;width:240px}
.news-field{left:363px;top:697px;width:179px;height:33px;border:1px solid var(--line);font-size:11px;color:var(--muted);padding-left:12px;line-height:31px}
.btn.subscribe{left:551px;top:697px;width:34px;height:33px}
.meta{left:620px;top:665px;list-style:none;font-size:11.5px;color:var(--ink)}
.meta li{height:25.3px;display:flex;align-items:center;gap:12px}
.meta li::before{content:"";border-left:4px solid #8b9398;border-top:3.5px solid transparent;border-bottom:3.5px solid transparent}
.social{left:780px;top:671px;display:flex;gap:10px}
.social span{width:24px;height:24px;border-radius:50%;background:#9aa2a7}
.social span.hot{background:var(--yellow)}
.copy{left:945px;top:669px;width:170px}
.brand-small{left:945px;top:724px;font:900 17px/17px 'Lato',sans-serif;color:var(--yellow)}
</style>
</head>
<body>
<div class="abs top-rule"></div>
<header class="abs header"></header>
<div class="abs brand">Plim<br>vota</div>
<div class="abs tagline">Generate your<br>own QR Code</div>

<div class="abs field user">
  <svg width="11" height="11" viewBox="0 0 11 11"><circle cx="5.5" cy="3" r="2.6" fill="#b3babe"/><path d="M0.5 11c0-3 2.2-4.6 5-4.6s5 1.6 5 4.6z" fill="#b3babe"/></svg>
  Username...
</div>
<div class="abs field pass">
  <svg width="11" height="11" viewBox="0 0 11 11"><circle cx="5.5" cy="3" r="2.6" fill="#b3babe"/><path d="M0.5 11c0-3 2.2-4.6 5-4.6s5 1.6 5 4.6z" fill="#b3babe"/></svg>
  Password...
</div>
<div class="abs btn login">
  <svg width="15" height="15" viewBox="0 0 15 15" fill="none" stroke="#fff" stroke-width="1.6"><path d="M8 2h5v11H8"/><path d="M1.5 7.5h8M6.5 4.5l3 3-3 3"/></svg>
</div>
<div class="abs account-links">Forgot password?<span>Register new account</span></div>

<div class="abs nav-band"></div>
<nav class="abs nav">
  <div class="nav-item active" style="width:117px">HOME
    <svg width="10" height="6" viewBox="0 0 10 6"><path d="M0 0h10L5 6z" fill="#3d4347"/></svg>
  </div>
  <div class="nav-item" style="width:119px">QR CODES</div>
  <div class="nav-item" style="width:109px">ABOUT US</div>
  <div class="nav-item" style="width:91px">FAQ</div>
  <div class="nav-item" style="width:107px">CONTACT</div>
</nav>

<main>
<div class="abs stage"></div>
<h1 class="abs section-title">MAKE YOUR OWN <b>QR CODE</b></h1>
<svg class="abs title-pointer" width="16" height="9" viewBox="0 0 16 9"><path d="M0 0h16L8 9z" fill="#f4c20d"/></svg>
<div class="abs section-rule"></div>

<div class="abs steps">
  <div class="step active"><span class="step-num">1</span>Select data type</div>
  <div class="step"><span class="step-num">2</span>Select content</div>
  <div class="step"><span class="step-num">3</span>Upload image</div>
  <div class="step"><span class="step-num">4</span>Draw a Square</div>
  <div class="step"><span class="step-num">5</span>DOWNLOAD</div>
</div>
<div class="abs panel"></div>
<ul class="abs type-list col-a">
  <li>Website URL</li><li>Vidora Video</li><li>Terrano Maps Location</li><li>Chirpline</li><li>Pallbook</li>
</ul>
<ul class="abs type-list col-b">
  <li>Website URL</li><li class="selected">Vidora Video</li><li>Terrano Maps Location</li><li>Chirpline</li><li>Pallbook</li>
</ul>
<ul class="abs type-list col-c">
  <li>Website URL</li><li>Vidora Video</li><li>Terrano Maps Location</li><li>Chirpline</li><li>Pallbook</li>
</ul>
</main>

<footer>
<div class="abs footer-rule"></div>
<h3 class="abs footer-heading" style="left:112px">WHAT'S A QR CODE?</h3>
<p class="abs footer-text about">A QR Code (It stands for "Quick Response") is a cell phone <b>readable</b> bar code that can store website URL's, plain text, phone numbers, <b>email addresses</b> and pretty much any other alphanumeric data.</p>

<h3 class="abs footer-heading" style="left:361px">NEWSLETTER</h3>
<p class="abs footer-text news-note">Be up to date with signup to our <b>newsletter</b>.</p>
<div class="abs news-field">your adress e-mail...</div>
<div class="abs btn subscribe">
  <svg width="15" height="15" viewBox="0 0 15 15" fill="none" stroke="#fff" stroke-width="1.6"><path d="M8 2h5v11H8"/><path d="M1.5 7.5h8M6.5 4.5l3 3-3 3"/></svg>
</div>

<h3 class="abs footer-heading" style="left:611px">META</h3>
<ul class="abs meta">
  <li>Home</li><li>QR Codes</li><li>About Us</li><li>FAQ</li><li>Contact</li>
</ul>

<h3 class="abs footer-heading" style="left:780px">SOCIAL</h3>
<div class="abs social" aria-label="Social links">
  <span></span><span></span><span class="hot"></span><span></span>
</div>

<h3 class="abs footer-heading" style="left:945px">COPYRIGHT</h3>
<p class="abs footer-text copy">Copyright (C) 2014 by Plimvota.net. All Right Reserved.</p>
<div class="abs brand-small">Plim<br>vota</div>
</footer>
</body>
</html>
```